Book Cover design for Tomely and print book.

I’m looking for a unique and fresh approach for this book cover design because the content has a unique and fresh approach. For example I don't want a design that has steps, bulls eyes, targets or trophies. Because it incorporates some of the spiritual elements of goal setting I’d like it to encompass my signature purple colour #330066.

Think about people who want to set unrealistic or aspirational goals that will change the world - rather than people who want to achieve a simple goal.

I want a cover that will work for Tomely and for a print book, and, possibly later, a workbook.

NB My company logo is not intended to go onto the book, it's for your information only. However, an ISBN number will be included.

Target Market(s)

20-60 year old professional men and women who are motivated and want to achieve huge, aspirational goals while enjoying the journey.

Font styles to use
Serif
Sans Serif
Other font styles liked:
• I use Agenda in my manuals, but this isn't essential.

Requirements
Must have
• I prefer rounded shapes rather than sharp angles - but I'm pretty open to new designs. I also prefer font to be set in a combination of upper and lower case letters.
Nice to have
• purple colour #330066 if possible. I don't expect this to be all over the cover. Taking a quick look at my website http://quillfernworks.co.nz might help. Otherwise I'm open to colour, but not a fan of green.
• I like the cleverness and simplicity of Hooked by Wonder, (http://www.bookvarlo-example.com/Hooked-Wonder-Linger-Others-published/dp/Q7R2K9P1ZX/ref=sr_1_4?s=books&ie=UTF8&qid=7302915586&sr=1-4&keywords=Hooked+by+Wonder) In fact all the book covers of Marlo and Teo Brannick's books are impressive.
Should not have
• Bulls eyes, steps, targets or other symbols traditionally associated with goal setting.

```html
<!DOCTYPE html>
<html lang="en">
<head>
<meta charset="utf-8">
<title>Vast Visions – Book Cover Spread</title>
<link rel="stylesheet" href="https://fonts.googleapis.com/css2?family=Cabin:wght@400;500;600;700&display=swap">
<style>
  :root {
    --signature-purple: #330066;
    --title-purple: #3b0d6e;
    --paper: #ffffff;
    --stage: #e3e7e2;
    --ink: #222222;
    --sky-top: #1d2a63;
    --sky-mid: #5a3d8a;
    --sky-glow: #d9703a;
    --sky-sun: #f3a43a;
    --accent-dot: #8a2b8f;
  }
  * { margin: 0; padding: 0; box-sizing: border-box; }
  html, body {
    width: 1200px; height: 720px; overflow: hidden;
    background: var(--stage);
    font-family: "Cabin", sans-serif;
  }
  .spread {
    position: absolute; left: 189px; top: 40px;
    width: 822px; height: 640px;
    background: var(--paper);
    display: flex;
  }
  .back-cover {
    position: relative; width: 420px; height: 100%;
    text-align: center; color: var(--ink);
  }
  .back-title {
    position: absolute; top: 86px; left: 0; right: 0;
    color: var(--title-purple);
  }
  .back-title .main { font-size: 23px; font-weight: 700; line-height: 1.1; }
  .back-title .sub { font-size: 13px; font-weight: 700; line-height: 1.3; margin-top: 4px; }
  .back-title .strap { font-size: 13px; font-weight: 400; line-height: 1.3; margin-top: 10px; }
  .blurb {
    position: absolute; top: 214px; left: 66px; right: 66px;
    font-size: 8.2px; line-height: 12px;
  }
  .blurb p { margin-bottom: 12px; }
  .blurb strong { font-weight: 700; }
  .publisher {
    position: absolute; top: 540px; left: 0; right: 0;
    display: flex; justify-content: center; align-items: center; gap: 6px;
  }
  .publisher-name { font-size: 12px; font-weight: 500; color: var(--title-purple); }
  .publisher-dot { width: 14px; height: 14px; border-radius: 50%; background: var(--accent-dot); }
  .publisher-url {
    position: absolute; top: 588px; left: 0; right: 0;
    font-size: 8px; font-weight: 700;
  }
  .front-cover { position: relative; width: 402px; height: 100%; overflow: hidden; }
  .front-art { position: absolute; inset: 0; }
  .front-title {
    position: absolute; top: 82px; left: 0; right: 0;
    text-align: center; color: var(--paper);
  }
  .front-title .word-one { font-size: 92px; font-weight: 700; line-height: 0.9; letter-spacing: 1px; }
  .front-title .word-two { font-size: 50px; font-weight: 700; line-height: 1.1; letter-spacing: 2px; margin-top: 4px; }
  .front-title .principles {
    font-size: 23px; font-weight: 700; line-height: 1.3; letter-spacing: 2.5px; margin-top: 12px;
  }
  .front-strap {
    position: absolute; top: 456px; left: 0; right: 0;
    text-align: center; color: var(--signature-purple);
    font-size: 18px; font-weight: 700; line-height: 1.3;
  }
  .front-author {
    position: absolute; top: 574px; left: 0; right: 0;
    text-align: center; color: var(--paper);
    font-size: 20px; font-weight: 500; letter-spacing: 0.5px;
  }
</style>
</head>
<body>
  <div class="spread">
    <section class="back-cover">
      <div class="back-title">
        <div class="main">VAST VISIONS:</div>
        <div class="sub">7 PRINCIPLES TO REALISE<br>AMBITIOUS DREAMS</div>
        <div class="strap">USING THE R.A.D.I.A.N.T. METHOD<br>TO SHAPE YOUR TOMORROW</div>
      </div>
      <div class="blurb">
        <p>If a big dream has ever slipped through your fingers –<br>(and honestly – whose hasn't?) then this guide is for you.</p>
        <p>By working through the 7 principles behind the R.A.D.I.A.N.T. method you'll fill the gaps that ordinary planning systems leave open. Use the method to chase wildly ambitious visions; visions that will push you to learn and expand while you enjoy every single step of the road towards the life you imagine.</p>
        <p>R.A.D.I.A.N.T. planning reveals why certain dreams can feel like a long uphill trudge through thick mud, in the rain, with no end in sight! You discover how to shape visions that, while testing you, also feel light and joyful. The R.A.D.I.A.N.T. method blends fresh findings from brain science with time-honoured and reflective insight. It's full of stories that bring each principle to life.</p>
        <p><strong>ROSALIND ASHCOMBE</strong> is a widely respected author, senior facilitator and life mentor. In this guide, she draws on two decades of practice to show you what helps, as well as what simply gets in the way of building the future you want.</p>
      </div>
      <div class="publisher">
        <span class="publisher-name">Quillfern Works</span>
        <span class="publisher-dot"></span>
      </div>
      <div class="publisher-url">www.quillfernworks.co.nz</div>
    </section>

    <section class="front-cover">
      <svg class="front-art" width="402" height="640" viewBox="0 0 402 640">
        <defs>
          <linearGradient id="night-sky" x1="0" y1="0" x2="0.3" y2="1">
            <stop offset="0" stop-color="var(--sky-top)"/>
            <stop offset="0.45" stop-color="var(--sky-mid)"/>
            <stop offset="0.78" stop-color="var(--sky-glow)"/>
            <stop offset="1" stop-color="var(--sky-sun)"/>
          </linearGradient>
        </defs>
        <circle cx="200" cy="245" r="212" fill="url(#night-sky)" role="img"
                aria-label="Starry night sky over a mountain ridge with a figure pointing upward at sunrise"/>
        <rect x="0" y="459" width="402" height="181" fill="var(--signature-purple)"/>
        <path d="M0 459 Q201 650 402 459 L402 440 L0 440 Z" fill="var(--paper)"/>
      </svg>
      <div class="front-title">
        <div class="word-one">VAST</div>
        <div class="word-two">VISIONS:</div>
        <div class="principles">7 PRINCIPLES<br>TO REALISE<br>AMBITIOUS<br>DREAMS</div>
      </div>
      <div class="front-strap">Using the R.A.D.I.A.N.T. method<br>to shape your tomorrow</div>
      <div class="front-author">ROSALIND ASHCOMBE</div>
    </section>
  </div>
</body>
</html>
```